Trucking company specializing in intermodal containers

We need a logo design for our trucking company based in Kent, Washington. Our companies name is Dorvale Haulworks LLC, we specialize in intermodal containers, and work off of the Crestmark rail lines and the ports. We provide service by transporting freight with our fleet of trucks. We operate within Washington, Oregon, and Idaho. Our fleet consists of an east division and a local division. Our team motto currently is globally connected, locally invested.

Target Market(s)

brokers, intermodal management companies, customers

Industry/Entity Type

Trucking Company

Contact Information for Business Card

physical address 4519 N. 163rd Pl Kent, WA 98517
office number is 253-614-9026

Font styles to use
Sans Serif

Colors

Designer to choose colors to be used in the design.

Requirements
Must have
• We need to update our current logo. Something like an emblem; that makes a statement that this logo/ sign represents Dorvale Haulworks. Something like a royal stamp but in this case a royal shield.
Nice to have
• simple, yet bold. something someone does not currently have. We need something fresh and exciting. Something that will also make a statement because currently our reputation is great within the industry and our community. But we need to reflect that we are professional and willing to provide the best service. We are open to new statement lines.
Should not have
• Should not have something thats been used before. We are open to suggestions that you have and a design that is completely unique and you make originally without what we want but what you like as well. Ofcourse it should still represent the industry we are in.

```html
<!DOCTYPE html>
<html lang="en">
<head>
<meta charset="utf-8">
<title>Dorvale Haulworks LLC — Business Card</title>
<link rel="stylesheet" href="https://fonts.googleapis.com/css2?family=Cinzel:wght@700&family=Open+Sans:wght@400;600;700&display=swap">
<style>
  :root {
    --backdrop: #2e2927;
    --card-white: #f7f6f4;
    --brand-red: #9e0b0f;
    --brand-red-deep: #7e0709;
    --ink: #2b2b2b;
    --ink-soft: #555555;
    --on-red: #f4f4f4;
  }
  * { box-sizing: border-box; margin: 0; padding: 0; }
  html, body {
    width: 1200px; height: 844px; overflow: hidden;
    background: var(--backdrop);
  }
  .stage {
    position: relative; width: 1200px; height: 844px;
    display: flex; align-items: center; justify-content: center; gap: 40px;
  }
  .card {
    position: relative; width: 525px; height: 300px;
    border-radius: 4px; overflow: hidden;
    box-shadow: 0 10px 30px rgba(0,0,0,0.45);
  }
  .card--front { background: var(--card-white); }
  .card--back {
    background: radial-gradient(ellipse at 40% 40%, #b3161b 0%, var(--brand-red) 55%, var(--brand-red-deep) 100%);
    display: flex; align-items: center; justify-content: center;
  }
  .wordmark {
    display: flex; align-items: center; gap: 12px;
    font-family: "Open Sans", sans-serif; font-weight: 700;
    white-space: nowrap;
  }
  .wordmark__dot { border-radius: 50%; flex: none; }
  .card--front .wordmark {
    position: absolute; top: 36px; left: 150px;
    color: var(--brand-red); font-size: 24px;
  }
  .card--front .wordmark__dot { width: 34px; height: 34px; background: var(--brand-red); }
  .card--back .wordmark { color: var(--on-red); font-size: 30px; }
  .card--back .wordmark__dot { width: 44px; height: 44px; background: var(--on-red); }
  .contact {
    position: absolute; left: 40px; bottom: 26px;
    font-family: "Open Sans", sans-serif; color: var(--ink);
  }
  .contact__name {
    font-family: "Cinzel", serif; font-weight: 700;
    color: var(--brand-red); font-size: 17px; line-height: 22px; letter-spacing: 0.5px;
  }
  .contact__role { font-size: 13px; line-height: 18px; color: var(--ink-soft); }
  .contact__list { list-style: none; margin-top: 12px; font-size: 14px; line-height: 21px; }
  .contact__list li { display: flex; align-items: center; gap: 8px; }
  .contact__list svg { width: 12px; height: 12px; fill: var(--brand-red); flex: none; }
  .contact__address { font-size: 14px; line-height: 20px; margin-top: 12px; }
</style>
</head>
<body>
<main class="stage">
  <section class="card card--front" aria-label="Business card front">
    <div class="wordmark">
      <span class="wordmark__dot"></span>
      <span class="wordmark__name">Dorvale Haulworks LLC</span>
    </div>
    <div class="contact">
      <p class="contact__name">MARCUS ELLERY</p>
      <p class="contact__role">Managing Director</p>
      <ul class="contact__list">
        <li><svg viewBox="0 0 24 24" aria-hidden="true"><path d="M6.6 10.8a15 15 0 0 0 6.6 6.6l2.2-2.2a1 1 0 0 1 1-.25 11.4 11.4 0 0 0 3.6.57 1 1 0 0 1 1 1V20a1 1 0 0 1-1 1A17 17 0 0 1 3 4a1 1 0 0 1 1-1h3.5a1 1 0 0 1 1 1c0 1.25.2 2.45.57 3.57a1 1 0 0 1-.25 1z"/></svg>253-614-9026</li>
        <li><svg viewBox="0 0 24 24" aria-hidden="true"><path d="M2 5h20v2l-10 7L2 7z M2 9.5l10 7 10-7V19H2z"/></svg>info@dorvalehaulworks.com</li>
        <li><svg viewBox="0 0 24 24" aria-hidden="true"><circle cx="12" cy="12" r="10"/></svg>www.dorvalehaulworks.com</li>
      </ul>
      <p class="contact__address">4519 N. 163rd Pl Kent, WA 98517</p>
    </div>
  </section>
  <section class="card card--back" aria-label="Business card back">
    <div class="wordmark">
      <span class="wordmark__dot"></span>
      <span class="wordmark__name">Dorvale Haulworks LLC</span>
    </div>
  </section>
</main>
</body>
</html>
```